TKR Website Overhaul. Complete new website look and function.

Need our website overhauled to be updated so it aligns better with our current cliental. We have competitors to compare to. The purpose of the site has changed and is no longer sales based. This site needs to qualify us and allow consultants and engineers to just discover our background and differentiators. I have attached a company profile from a recent project to provide a better idea. This profile is directed towards the specific project however so that would need to be edited out. Competitor websites that we would want to be comparable to would include: https://www.velmoran.com/ , https://brimleyconstruction.ca/ , https://www.tuskconstruction.ca/ , https://steadfastdiggers.com/ , https://www.hallowayconstruction.ca/. These are all competitors so nothing can be directly copied. I have attached our logo's however I don't think they need to be directly used on the site or maybe they need to be changed to not include color etc. We need to have a more professional look and these colorful logos are hard to pull that off with other than maybe the all gold TKR prime contracting logo with a rich dark green background or something. Green has been our main color over the years and the leaf follows us as the core item in logos. Go with a gold leaf look or something. Our main focus is General Contracting (Prime Contracting) and civil construction. We are a home builder however we would do a second website for that so we don't want to include it. I don't mind a ton of generic civil and general contractor information etc on the site. I don't really need a portfolio of pictures showing on the site but job history etc is very common in the industry and that information can be found in the company profile attached. First Nation work is a big part of our portfolio but we have worked in mining, industrial, oil and gas as well. Municipal sewer and water is our main focus for civil construction though and is a big part of our First Nation work as well.

Industry/Entity Type

General Contractor and Civil Construction

Coding

Coded - Design and coding required

Number of Pages Required

5+ page

Font styles to use
Other font styles liked:
• A mix of Times New Roman, script and serif to create a very professional with a touch of elegance to match our leafed prime contractor logo.

Colors
00AB8E
00BBA5
67D7C9
C6EFE9
E9F9F6

Requirements
Must have
• A rich high end professional look. This company completes government work and is often looked at by executives. A menu that includes About, Our Work, Methodology, Join Our Team and Contact
Nice to have
• Some generic general pictures of municipal underground water work and general contractor building work. I am looking for a rich green darker greens where it matters but with more real world feel overall. So images and movement is good. Civil underground water and sewer, storm water, retention ponds, and process plant and electrical (such as water treatment plants), background imagery is good to have. I like to have things faded out in the background more than in your face.
Should not have
• brighter colors.

```html
<!DOCTYPE html>
<html lang="en">
<head>
<meta charset="utf-8">
<title>TKR Prime Contracting</title>
<link href="https://fonts.googleapis.com/css2?family=Playfair+Display:wght@600;700&family=Montserrat:wght@400;500;600&display=swap" rel="stylesheet">
<style>
:root{
  --ink:#0c0f0e;
  --ink-2:#131816;
  --forest:#0a2a1e;
  --forest-2:#0d3626;
  --green-line:#1f8a5a;
  --gold:#c9a03c;
  --gold-soft:#d8b65c;
  --text:#e9ece9;
  --muted:#a9b0ac;
  --rule:#2a302d;
}
*{margin:0;padding:0;box-sizing:border-box}
html,body{width:1200px;height:3628px;overflow:hidden;background:var(--ink);color:var(--text);font-family:"Montserrat",sans-serif}
.page{position:relative;width:1200px;height:3628px}
.serif{font-family:"Playfair Display",serif}

/* header */
.site-header{position:absolute;top:0;left:0;width:1200px;height:80px;background:linear-gradient(180deg,#0a2418 0%,rgba(10,36,24,.85) 100%);display:flex;align-items:center;justify-content:space-between;padding:0 50px 0 40px;z-index:3}
.brand{font-family:"Playfair Display",serif;font-weight:700;font-size:30px;color:var(--gold);letter-spacing:2px;display:flex;align-items:center;gap:10px}
.brand-mark{width:14px;height:14px;background:var(--gold)}
.main-nav{display:flex;align-items:center;gap:40px;font-size:14px;font-weight:500}
.main-nav a{color:var(--text);text-decoration:none}
.btn{display:inline-block;background:var(--gold);color:#111;font-size:13px;font-weight:600;padding:11px 22px;text-decoration:none}

/* hero */
.hero{position:absolute;top:0;left:0;width:1200px;height:640px}
.hero-photo{position:absolute;inset:0;background:radial-gradient(ellipse at 60% 70%,rgba(200,140,60,.35),transparent 55%),linear-gradient(180deg,#3a3a36 0%,#25241f 45%,#14120e 100%)}
.hero-shade{position:absolute;inset:0;background:linear-gradient(180deg,rgba(0,0,0,.15),rgba(0,0,0,.55))}
.hero-copy{position:absolute;top:220px;left:0;width:1200px;text-align:center}
.hero-title{font-family:"Playfair Display",serif;font-weight:700;font-size:50px;line-height:1.15;letter-spacing:1px;text-transform:uppercase}
.hero-sub{font-size:14px;line-height:1.5;margin:14px auto 30px;width:460px;color:#dcdcd6}

/* wedge + arrow */
.wedge{position:absolute;top:600px;left:0;width:1200px;height:200px}
.down-arrow{position:absolute;top:660px;left:584px}

/* about */
.about-photo{position:absolute;top:905px;left:148px;width:400px;height:415px;background:linear-gradient(135deg,#e6e4df 0%,#c9c5bd 60%,#a9a397 100%)}
.about-copy{position:absolute;top:955px;left:612px;width:430px}
.section-title{font-family:"Playfair Display",serif;font-weight:700;font-size:38px;line-height:1.15;text-transform:uppercase}
.about-copy p{font-size:13px;line-height:1.65;color:var(--muted);margin:22px 0 26px}

/* services */
.services-title{position:absolute;top:1400px;left:0;width:1200px;text-align:center}
.service-card{position:absolute;top:1500px;width:336px}
.service-img{height:262px}
.service-card h3{font-family:"Playfair Display",serif;font-weight:700;font-size:17px;text-transform:uppercase;margin-top:24px;text-align:center}
.service-card p{font-size:12px;line-height:1.5;color:var(--muted);text-align:center;margin-top:6px;padding:0 40px}
.slider-arrows{position:absolute;top:1880px;left:550px;display:flex;gap:40px}

/* approach */
.approach{position:absolute;top:2010px;left:0;width:1200px;height:350px;background:radial-gradient(ellipse at 50% 40%,#0f3a28 0%,#0a2a1d 55%,#071c14 100%)}
.approach .section-title{text-align:center;margin-top:60px}
.approach-track{position:absolute;top:180px;left:240px;width:720px;height:2px;background:var(--gold)}
.step{position:absolute;top:156px;width:200px;text-align:center;margin-left:-100px}
.step-num{display:inline-block;width:48px;height:48px;line-height:48px;background:var(--gold);color:#111;font-family:"Playfair Display",serif;font-weight:700;font-size:20px}
.step p{font-size:12px;line-height:1.5;margin-top:14px;color:var(--text)}

/* projects */
.projects{position:absolute;top:2360px;left:0;width:1200px}
.projects .section-title{text-align:center;margin-top:85px}
.projects-intro{text-align:center;font-size:12px;color:var(--muted);width:460px;margin:14px auto 0;line-height:1.5}
.project-table{position:absolute;top:240px;left:100px;width:1000px;border-collapse:collapse}
.project-table th{font-family:"Playfair Display",serif;font-weight:600;font-size:15px;color:var(--gold);text-align:left;letter-spacing:1px;padding:0 0 22px;border-bottom:2px solid var(--gold)}
.project-table td{font-family:"Playfair Display",serif;font-weight:700;font-size:15px;text-transform:uppercase;padding:28px 0;height:96px;border-bottom:1px solid var(--rule);vertical-align:middle}
.project-table td.deliverable{font-family:"Montserrat",sans-serif;font-weight:400;font-size:12px;text-transform:none;color:var(--muted);line-height:1.5;width:260px}
.col-cat{width:380px}.col-sector{width:360px}

/* footer */
.footer-v{position:absolute;top:3250px;left:0;width:1200px;height:130px}
.site-footer{position:absolute;top:3340px;left:0;width:1200px;height:288px;background:var(--forest)}
.site-footer .brand{position:absolute;top:60px;left:60px;font-size:44px}
.footer-nav{position:absolute;top:100px;right:60px;display:flex;gap:34px;font-size:13px}
.footer-nav a{color:var(--text);text-decoration:none}
.footer-contact{position:absolute;top:150px;right:60px;display:flex;gap:30px;font-size:12px;color:var(--text)}
.footer-contact span{display:flex;align-items:center;gap:8px}
.footer-bottom{position:absolute;bottom:0;left:0;width:1200px;height:54px;border-top:1px solid rgba(255,255,255,.12);display:flex;align-items:center;justify-content:space-between;padding:0 60px;font-size:12px;color:var(--muted)}
</style>
</head>
<body>
<div class="page">

  <section class="hero">
    <div class="hero-photo" role="img" aria-label="Dusk view of a city street under construction with cranes and lights"></div>
    <div class="hero-shade"></div>
    <div class="hero-copy">
      <h1 class="hero-title">Bridging Excellence in Civil<br>&amp; Prime Contracting.</h1>
      <p class="hero-sub">Partnering with Government, Industry, and First Nations to deliver sustainable infrastructure for the future.</p>
      <a class="btn" href="#">Explore Our Methodology</a>
    </div>
  </section>

  <header class="site-header">
    <div class="brand"><span class="brand-mark"></span>TKR Construction</div>
    <nav class="main-nav">
      <a href="#">Home</a><a href="#">About Us</a><a href="#">Our Work</a><a href="#">Methodology</a><a href="#">Join Our Team</a>
      <a class="btn" href="#">Contact Us</a>
    </nav>
  </header>

  <svg class="wedge" viewBox="0 0 1200 200" preserveAspectRatio="none">
    <polygon points="0,40 600,160 1200,40 1200,200 0,200" fill="#0c0f0e"/>
    <polygon points="0,40 600,160 1200,40 1200,60 600,180 0,60" fill="#0a2a1d"/>
  </svg>
  <svg class="down-arrow" width="32" height="48" viewBox="0 0 32 48"><path d="M16 2v42M4 32l12 12 12-12" stroke="#ffffff" stroke-width="3" fill="none"/></svg>

  <div class="about-photo" role="img" aria-label="Engineer's hand drafting construction plans on paper"></div>
  <div class="about-copy">
    <h2 class="section-title">Proven Expertise.<br>Government Trusted.</h2>
    <p>TKR Prime Contracting is more than a general contractor. We specialize in complex civil construction, municipal water systems, and industrial infrastructure. Our focus is on qualifying for elite projects through high-end methodology and a legacy of trust with government executives and mining partners.</p>
    <a class="btn" href="#">Read More</a>
  </div>

  <h2 class="section-title services-title">Our Services</h2>
  <article class="service-card" style="left:72px">
    <div class="service-img" role="img" aria-label="City skyline with towers under construction" style="background:linear-gradient(180deg,#b9c3cc 0%,#6e7680 55%,#3e4046 100%)"></div>
    <h3>Municipal Infrastructure</h3>
    <p>Expertise in sewer, water lines, and storm water management.</p>
  </article>
  <article class="service-card" style="left:432px">
    <div class="service-img" role="img" aria-label="Workers on a construction site at sunset with cranes" style="background:linear-gradient(180deg,#e2a35a 0%,#b06a35 50%,#4a3022 100%)"></div>
    <h3>Civil Construction</h3>
    <p>Heavy earthworks, retention ponds, and site preparation.</p>
  </article>
  <article class="service-card" style="left:792px">
    <div class="service-img" role="img" aria-label="Team reviewing project plans around a table" style="background:linear-gradient(180deg,#f0eee9 0%,#cfc9bf 60%,#9e978b 100%)"></div>
    <h3>First Nation Partnerships</h3>
    <p>A core part of our portfolio, delivering vital infrastructure to Indigenous communities.</p>
  </article>
  <div class="slider-arrows">
    <svg width="36" height="16" viewBox="0 0 36 16"><path d="M34 8H3M10 1L3 8l7 7" stroke="#fff" stroke-width="2" fill="none"/></svg>
    <svg width="36" height="16" viewBox="0 0 36 16"><path d="M2 8h31M26 1l7 7-7 7" stroke="#fff" stroke-width="2" fill="none"/></svg>
  </div>

  <section class="approach">
    <h2 class="section-title">The TKR Approach.</h2>
    <div class="approach-track"></div>
    <div class="step" style="left:240px"><span class="step-num">01</span><p>Strategic Planning And<br>Execution.</p></div>
    <div class="step" style="left:480px"><span class="step-num">02</span><p>Environmental Steward-<br>ship.</p></div>
    <div class="step" style="left:720px"><span class="step-num">03</span><p>Government &amp; Safety<br>Compliance.</p></div>
    <div class="step" style="left:960px"><span class="step-num">04</span><p>Indigenous Engagement &amp;<br>Collaboration.</p></div>
  </section>

  <section class="projects">
    <h2 class="section-title">Selected Project History.</h2>
    <p class="projects-intro">As professional hold as a joint general prime trade projects (Mining, Oil &amp; Gas, Municipal) we have delivered across the region.</p>
    <table class="project-table">
      <thead><tr><th class="col-cat">PROJECT CATEGORY</th><th class="col-sector">SECTOR</th><th>PRIMARY DELIVERABLES</th></tr></thead>
      <tbody>
        <tr><td>Municipal Sewer &amp; Water</td><td>Municipal / Government</td><td class="deliverable">Deep bury utility installation, main line extensions, and lift station integration.</td></tr>
        <tr><td>First Nation Infrastructure</td><td>Indigenous Communities</td><td class="deliverable">Community water distribution systems &amp; sustainable storm water management.</td></tr>
        <tr><td>Mining Site Development</td><td>Industrial / Mining</td><td class="deliverable">Heavy earthworks, retention pond construction, and site access road development.</td></tr>
        <tr><td>Oil &amp; Gas Process Support</td><td>Energy / Oil &amp; Gas</td><td class="deliverable">Facility site preparation, electrical process plant civil works, and containment systems.</td></tr>
        <tr><td>Water Treatment Facilities</td><td>Municipal / Process</td><td class="deliverable">Structural civil work for treatment plants and complex underground piping networks.</td></tr>
      </tbody>
    </table>
  </section>

  <svg class="footer-v" viewBox="0 0 1200 130" preserveAspectRatio="none">
    <polygon points="0,90 600,20 1200,90 1200,130 0,130" fill="#0a2a1e"/>
    <polyline points="0,90 600,20 1200,90" stroke="#1f8a5a" stroke-width="4" fill="none"/>
  </svg>

  <footer class="site-footer">
    <div class="brand"><span class="brand-mark"></span>TKR Construction</div>
    <nav class="footer-nav"><a href="#">Home</a><a href="#">About Us</a><a href="#">Our Work</a><a href="#">Methodology</a><a href="#">Join Our Team</a></nav>
    <div class="footer-contact">
      <span><svg width="14" height="14" viewBox="0 0 24 24"><path d="M6.6 10.8a15 15 0 006.6 6.6l2.2-2.2a1 1 0 011-.25 11.4 11.4 0 003.6.57 1 1 0 011 1V20a1 1 0 01-1 1A17 17 0 013 4a1 1 0 011-1h3.5a1 1 0 011 1c0 1.25.2 2.45.57 3.57a1 1 0 01-.25 1z" fill="#c9a03c"/></svg>(403) 555-0148</span>
      <span><svg width="12" height="16" viewBox="0 0 12 16"><path d="M6 0a6 6 0 00-6 6c0 4.5 6 10 6 10s6-5.5 6-10a6 6 0 00-6-6zm0 8.2A2.2 2.2 0 116 3.8a2.2 2.2 0 010 4.4z" fill="#c9a03c"/></svg>Harlow Ridge Enterprises Ltd. Box 220 Ridgeford, Alberta T0A 1B0</span>
    </div>
    <div class="footer-bottom"><span>© 2026 TKR Prime Contracting. All Rights Reserved.</span><span>Privacy Policy</span></div>
  </footer>

</div>
</body>
</html>
```